Brightwater Partners Inc. Business Cards

We provide services for executives in mid-sized ($250M - $1B) and large companies ($1B +) for who manage their indirect channels. Indirect channels are when 3rd parties that sell a companies products. Examples are the managers in companies that supervise agent, dealer, reseller channels including insurance, auto dealers, technology resellers, and other agent and dealer channels. These services (the Four Pillars) include attracting the best channel resellers, advancing their skills, activating inactive resellers, awarding your resellers with compensation and incentives, and advertising your channel with new marketing
Updates

Thank you for your designs - they all look great.  I realize that I forgot to include a few items.  The items below need to be added to my card design:

Dennis Latham
CEO / Founder
(This is above the address)
(Below the address) (use email & Website icon)
dennis.latham@brightwaterpartners.example
website:  www.brightwaterpartners.example
(Note:  Please use icon from Twitter, Linkedin, and Skype)
(Twitter) #BrightwaterPtnrs
(Skype):  dennisalanlatham

Target Market(s)

Business Executives responsible for their indirect channel

Industry/Entity Type

Advertising

Contact Information for Business Card

PO Box 419
2854 Hollister Lane
Alderbrook VT 05999 USA
+1 508.555.0193

Colors

Designer to choose colors to be used in the design.

Requirements
Must have
• Front: I'd prefer a simple design - white background. Logo, contact information, and tag line "Forging Stronger Networks" I have provided two logos 1) The plain logo "Brightwater Partners" (Front of card) and 2) "The Four Pillars of Brightwater Partners" (Back of Card).
a) Front: Logo, tag line, contact info, b) Back: Graphic of four pillars; plus the following links.
Four Pillars of Brightwater Partners: http://www.brightwaterpartners.example/the-four-pillars/
Four Pillars Channel Audit:
http://www.brightwaterpartners.example/pillars-network-review/
Four Pillars Blog:
http://www.brightwaterpartners.example/category/blog/
Four Pillars Downloads:
http://www.brightwaterpartners.example/download-best-practices/
Nice to have
• Brightwater Partners logo on Front and Graphic of the "Four Pillars of Brightwater Partners" on the back. Match the colors of the logo.

```html
<!DOCTYPE html>
<html lang="en">
<head>
<meta charset="utf-8">
<title>Brightwater Partners Inc. Business Cards</title>
<link rel="stylesheet" href="https://fonts.googleapis.com/css2?family=Open+Sans:wght@300;400;600;700&display=swap">
<style>
  :root {
    --page-bg: #e9e9ea;
    --card-bg: #ffffff;
    --brand-blue: #2a5fc0;
    --brand-green: #76be3f;
    --text-grey: #7a7a7a;
    --tag-grey: #b4b4b4;
    --shadow: rgba(0, 0, 0, 0.18);
  }
  * { box-sizing: border-box; margin: 0; padding: 0; }
  html, body {
    width: 1200px;
    height: 575px;
    overflow: hidden;
    background: var(--page-bg);
    font-family: "Open Sans", Arial, sans-serif;
  }
  .canvas {
    position: relative;
    width: 1200px;
    height: 575px;
    display: flex;
    align-items: center;
    justify-content: center;
    gap: 60px;
  }
  .card {
    position: relative;
    width: 520px;
    height: 297px;
    background: var(--card-bg);
    box-shadow: 0 6px 18px var(--shadow);
    overflow: hidden;
  }

  /* Front */
  .card--front { padding: 30px 34px; }
  .brand {
    display: flex;
    align-items: center;
    gap: 12px;
  }
  .brand__mark {
    width: 44px;
    height: 44px;
    border-radius: 50%;
    background: var(--brand-green);
    flex: none;
  }
  .brand__name {
    font-size: 22px;
    font-weight: 700;
    letter-spacing: 1px;
    text-transform: uppercase;
    color: var(--brand-blue);
    line-height: 1;
    white-space: nowrap;
  }
  .tagline {
    margin: 6px 0 0 56px;
    font-size: 14px;
    font-weight: 700;
    color: var(--tag-grey);
  }
  .person {
    margin: 18px 0 0 56px;
  }
  .person__name {
    font-size: 21px;
    font-weight: 300;
    color: var(--brand-blue);
    text-transform: uppercase;
    letter-spacing: 0.5px;
    line-height: 1.1;
  }
  .person__title {
    font-size: 10px;
    color: var(--text-grey);
  }
  .contact-list {
    list-style: none;
    margin-top: 14px;
    font-size: 10.5px;
    color: var(--text-grey);
    line-height: 1.45;
  }
  .contact-list li {
    display: flex;
    align-items: flex-start;
    gap: 10px;
  }
  .contact-list .icon {
    width: 14px;
    height: 14px;
    flex: none;
    margin-top: 1px;
  }
  .social-list { margin-top: 8px; }
  .social-dot {
    width: 13px;
    height: 13px;
    border-radius: 50%;
    background: var(--brand-blue);
    flex: none;
    margin: 1px 1px 0 0;
  }

  /* Back */
  .card--back { padding: 30px 34px; }
  .brand--back { justify-content: flex-end; }
  .brand--back .brand__name { font-size: 16px; }
  .brand--back .brand__mark { width: 26px; height: 26px; }
  .link-list {
    list-style: none;
    margin-top: 22px;
  }
  .link-list li { margin-bottom: 12px; }
  .link-list__label {
    font-size: 11px;
    font-weight: 600;
    color: var(--brand-blue);
  }
  .link-list__url {
    font-size: 10.5px;
    color: var(--text-grey);
  }
</style>
</head>
<body>
<main class="canvas">

  <section class="card card--front" aria-label="Business card front">
    <div class="brand">
      <span class="brand__mark"></span>
      <span class="brand__name">Brightwater Partners</span>
    </div>
    <p class="tagline">Forging Stronger Networks</p>

    <div class="person">
      <p class="person__name">Dennis Latham</p>
      <p class="person__title">CEO / Founder</p>
    </div>

    <ul class="contact-list">
      <li>
        <svg class="icon" viewBox="0 0 14 14" aria-hidden="true">
          <circle cx="7" cy="7" r="7" fill="var(--brand-green)"/>
          <path d="M7 3.2a2.4 2.4 0 0 0-2.4 2.4c0 1.8 2.4 4.6 2.4 4.6s2.4-2.8 2.4-4.6A2.4 2.4 0 0 0 7 3.2z" fill="#fff"/>
          <circle cx="7" cy="5.6" r="0.9" fill="var(--brand-green)"/>
        </svg>
        <span>PO Box 419 2854 Hollister Lane<br>Alderbrook VT 05999 USA +1 508.555.0193</span>
      </li>
      <li>
        <svg class="icon" viewBox="0 0 14 14" aria-hidden="true">
          <rect width="14" height="14" rx="2" fill="var(--brand-green)"/>
          <rect x="3" y="4.2" width="8" height="5.6" fill="none" stroke="#fff" stroke-width="0.9"/>
          <path d="M3 4.4l4 3 4-3" fill="none" stroke="#fff" stroke-width="0.9"/>
        </svg>
        <span>dennis.latham@brightwaterpartners.example</span>
      </li>
      <li>
        <svg class="icon" viewBox="0 0 14 14" aria-hidden="true">
          <circle cx="7" cy="7" r="7" fill="var(--brand-green)"/>
          <circle cx="7" cy="7" r="4" fill="none" stroke="#fff" stroke-width="0.9"/>
          <ellipse cx="7" cy="7" rx="1.7" ry="4" fill="none" stroke="#fff" stroke-width="0.9"/>
          <line x1="3" y1="7" x2="11" y2="7" stroke="#fff" stroke-width="0.9"/>
        </svg>
        <span>www.brightwaterpartners.example</span>
      </li>
    </ul>

    <ul class="contact-list social-list">
      <li><span class="social-dot"></span><span>#BrightwaterPtnrs</span></li>
      <li><span class="social-dot"></span><span>www.profilehub.example/in/dennisalanlatham/</span></li>
      <li><span class="social-dot"></span><span>dennisalanlatham</span></li>
    </ul>
  </section>

  <section class="card card--back" aria-label="Business card back">
    <div class="brand brand--back">
      <span class="brand__mark"></span>
      <span class="brand__name">Brightwater Partners</span>
    </div>

    <ul class="link-list">
      <li>
        <p class="link-list__label">Four Pillars of Brightwater Partners:</p>
        <p class="link-list__url">www.brightwaterpartners.example/the-four-pillars/</p>
      </li>
      <li>
        <p class="link-list__label">Four Pillars Channel Audit:</p>
        <p class="link-list__url">www.brightwaterpartners.example/pillars-network-review/</p>
      </li>
      <li>
        <p class="link-list__label">Four Pillars Blog:</p>
        <p class="link-list__url">www.brightwaterpartners.example/category/blog/</p>
      </li>
      <li>
        <p class="link-list__label">Four Pillars Downloads:</p>
        <p class="link-list__url">www.brightwaterpartners.example/download-best-practices/</p>
      </li>
    </ul>
  </section>

</main>
</body>
</html>
```